Collaborative Business card design

I have a logo that I would like incorporate with my wife who is now a realtor as well.
Target Market(s)
Real Estate
Industry/Entity Type
Real Estate
Contact Information for Business Card
Names, Email accounts and phone numbers.. and Business info (required)
Font styles to use
Script
Colors
A7469A
B969AE
D3A5CF
EDDBEB
F8F0F9
Requirements
Must have
- Both Pictures and the logo from the previous business card

```html
<!DOCTYPE html>
<html lang="en">
<head>
<meta charset="utf-8">
<title>Harlan &amp; Marla Reed Real Estate – Business Card</title>
<link href="https://fonts.googleapis.com/css2?family=Cinzel:wght@400;600;700&family=Great+Vibes&family=Roboto:wght@400;500&display=swap" rel="stylesheet">
<style>
  :root{
    --bg:#2a2a2a;
    --plum:#a7469a;
    --orchid:#b969ae;
    --lilac:#d3a5cf;
    --blush:#eddbeb;
    --mist:#f8f0f9;
    --white:#ffffff;
    --photo-a:#b9a3b6;
    --photo-b:#6e4a68;
  }
  *{box-sizing:border-box;margin:0;padding:0}
  html,body{width:1200px;height:1015px;overflow:hidden;background:var(--bg)}
  body{position:relative;font-family:'Cinzel',serif}
  .card{position:absolute;left:250px;width:700px;height:400px;overflow:hidden;box-shadow:0 10px 30px rgba(0,0,0,.5)}
  .card--front{top:60px;background:var(--white)}
  .card--back{top:555px;background:var(--plum)}

  /* brand lockup */
  .brand{position:absolute;text-align:center}
  .brand__name{font-family:'Great Vibes',cursive;font-weight:400;line-height:1}
  .brand__sub{display:flex;align-items:center;justify-content:center;gap:12px;font-size:16px;letter-spacing:8px;margin-top:4px}
  .brand__sub::before,.brand__sub::after{content:"";width:40px;height:1px;background:currentColor}

  /* front */
  .card--front .brand{left:0;top:62px;width:700px;color:var(--plum)}
  .card--front .brand__name{font-size:72px}
  .card--front .brand__sub{color:var(--orchid)}
  .front-band{position:absolute;bottom:0}
  .front-band--services{left:0;width:400px;height:150px;background:var(--plum)}
  .front-band--brokerage{right:0;width:300px;height:185px;background:var(--orchid)}
  .services{position:absolute;left:40px;bottom:24px;list-style:none;color:var(--white);font-size:22px;font-weight:600;line-height:1.45}
  .services li::before{content:"";display:inline-block;width:7px;height:7px;border-radius:50%;background:var(--lilac);margin-right:12px;vertical-align:middle}
  .brokerage{position:absolute;right:0;bottom:62px;width:300px;padding:0 18px;display:flex;align-items:center;gap:10px;color:var(--white)}
  .brokerage__badge{flex:none;width:30px;height:30px;border:2px solid var(--white);border-radius:50%}
  .brokerage__name{font-size:14px;font-weight:600;line-height:1.25;white-space:nowrap}
  .brokerage__office{font-size:12px;line-height:1.3;border-left:1px solid var(--blush);padding-left:10px;white-space:nowrap}

  /* back */
  .address{position:absolute;left:40px;top:36px;display:flex;gap:12px;color:var(--white);font-size:16px;font-weight:600;line-height:1.3}
  .card--back .brand{left:20px;top:100px;width:330px;color:var(--white)}
  .card--back .brand__name{font-size:58px}
  .card--back .brand__sub{color:var(--blush);font-size:14px}
  .portraits{position:absolute;right:30px;top:26px}
  .agent-names{position:absolute;right:30px;top:192px;width:300px;display:flex;color:var(--white);font-family:'Great Vibes',cursive;font-size:32px}
  .agent-names span{width:150px;text-align:center}
  .contacts{position:absolute;left:40px;right:30px;bottom:28px;display:flex;justify-content:space-between;border-top:1px solid var(--lilac);padding-top:14px}
  .contact{list-style:none;color:var(--white);font-size:15px}
  .contact__who{font-size:13px;font-weight:600;letter-spacing:2px;color:var(--blush);margin-bottom:4px}
  .contact li{display:flex;align-items:center;gap:10px;margin-top:4px}
  .contact__phone{font-weight:600}
  .contact__email{font-family:'Roboto',sans-serif;font-weight:500}
</style>
</head>
<body>

<section class="card card--front">
  <div class="brand">
    <div class="brand__name">Harlan Reed</div>
    <div class="brand__sub">Real Estate</div>
  </div>

  <div class="front-band front-band--services"></div>
  <div class="front-band front-band--brokerage"></div>

  <ul class="services">
    <li>Residential</li>
    <li>Commercial</li>
    <li>Agricultural</li>
  </ul>

  <div class="brokerage">
    <span class="brokerage__badge"></span>
    <span class="brokerage__name">Summit Ridge<br>Realty</span>
    <span class="brokerage__office">Valley Homes &amp;<br>Properties</span>
  </div>
</section>

<section class="card card--back">
  <div class="address">
    <svg width="16" height="23" viewBox="0 0 18 26" aria-hidden="true">
      <path d="M9 0C4 0 0 4 0 9c0 6.5 9 17 9 17s9-10.5 9-17C18 4 14 0 9 0z" fill="var(--lilac)"/>
      <circle cx="9" cy="9" r="3.5" fill="var(--plum)"/>
    </svg>
    <p>780 Meadow Crest Suite 120<br>Riverton Idaho 83520</p>
  </div>

  <div class="brand">
    <div class="brand__name">Harlan Reed</div>
    <div class="brand__sub">Real Estate</div>
  </div>

  <svg class="portraits" width="300" height="164" viewBox="0 0 300 164">
    <defs>
      <radialGradient id="portraitTone" cx="45%" cy="40%" r="65%">
        <stop offset="0" stop-color="var(--photo-a)"/>
        <stop offset="1" stop-color="var(--photo-b)"/>
      </radialGradient>
    </defs>
    <circle cx="75" cy="82" r="76" fill="none" stroke="var(--lilac)" stroke-width="4"/>
    <circle cx="75" cy="82" r="70" fill="url(#portraitTone)" role="img" aria-label="Portrait photo of Harlan Reed"/>
    <circle cx="225" cy="82" r="76" fill="none" stroke="var(--lilac)" stroke-width="4"/>
    <circle cx="225" cy="82" r="70" fill="url(#portraitTone)" role="img" aria-label="Portrait photo of Marla Reed"/>
  </svg>

  <div class="agent-names">
    <span>Harlan Reed</span>
    <span>Marla Reed</span>
  </div>

  <div class="contacts">
    <ul class="contact">
      <li class="contact__who">Harlan</li>
      <li class="contact__phone">
        <svg width="16" height="16" viewBox="0 0 24 24" aria-hidden="true"><path d="M6.6 10.8a15 15 0 0 0 6.6 6.6l2.2-2.2a1 1 0 0 1 1-.25 11.4 11.4 0 0 0 3.6.57 1 1 0 0 1 1 1V20a1 1 0 0 1-1 1A17 17 0 0 1 3 4a1 1 0 0 1 1-1h3.5a1 1 0 0 1 1 1c0 1.25.2 2.45.57 3.57a1 1 0 0 1-.25 1z" fill="var(--lilac)"/></svg>
        208-555-0184
      </li>
      <li class="contact__email">
        <svg width="16" height="12" viewBox="0 0 20 16" aria-hidden="true"><rect width="20" height="16" rx="1" fill="var(--lilac)"/><path d="M1 1l9 7 9-7" fill="none" stroke="var(--plum)" stroke-width="1.6"/></svg>
        harlan@valleyhomesrealty.com
      </li>
    </ul>
    <ul class="contact">
      <li class="contact__who">Marla</li>
      <li class="contact__phone">
        <svg width="16" height="16" viewBox="0 0 24 24" aria-hidden="true"><path d="M6.6 10.8a15 15 0 0 0 6.6 6.6l2.2-2.2a1 1 0 0 1 1-.25 11.4 11.4 0 0 0 3.6.57 1 1 0 0 1 1 1V20a1 1 0 0 1-1 1A17 17 0 0 1 3 4a1 1 0 0 1 1-1h3.5a1 1 0 0 1 1 1c0 1.25.2 2.45.57 3.57a1 1 0 0 1-.25 1z" fill="var(--lilac)"/></svg>
        208-555-0197
      </li>
      <li class="contact__email">
        <svg width="16" height="12" viewBox="0 0 20 16" aria-hidden="true"><rect width="20" height="16" rx="1" fill="var(--lilac)"/><path d="M1 1l9 7 9-7" fill="none" stroke="var(--plum)" stroke-width="1.6"/></svg>
        marla@valleyhomesrealty.com
      </li>
    </ul>
  </div>
</section>

</body>
</html>
```